Business card design needed

Card needs to say

Maren Dulworth
Investor - Solutions - Development

My business is in property deals. I would like the words above to be on the card. I have attached a logo for you to copy/recreate.
On the back you could list the following:

Creative property solutions

Thankyou, Maren

Target Market(s)

people wanting to get into the property market, desperate sellers, Mums & Dads wanting to help their kids to purchase a property. People who want to create wealth. People who are stuck and need a solution.

Industry/Entity Type

Business

Contact Information for Business Card

T: 0481 253 407
F: (07) 3584 2719
E: maren47@plx.com.au

Requirements
Must have
• Simple and effective.
Look like I am here to help
Should not have
• Should not look like a realestate agent

```html
<!DOCTYPE html>
<html lang="en">
<head>
<meta charset="utf-8">
<title>Maren Dulworth — Business Card</title>
<link rel="stylesheet" href="https://fonts.googleapis.com/css2?family=Arimo:wght@700&display=swap">
<style>
  :root {
    --backdrop: #3b3b3b;
    --card-dark: #231f20;
    --card-light: #ececec;
    --brand-green: #7ab648;
    --text-grey: #8a8a8a;
    --text-dark-grey: #6f6f6f;
  }
  * { margin: 0; padding: 0; box-sizing: border-box; }
  html, body {
    width: 1200px;
    height: 900px;
    overflow: hidden;
    background: var(--backdrop);
    font-family: "Arimo", Arial, sans-serif;
    font-weight: 700;
  }
  .stage { position: relative; width: 1200px; height: 900px; }
  .card {
    position: absolute;
    top: 300px;
    width: 525px;
    height: 296px;
  }
  .card--front { left: 58px; background: var(--card-dark); }
  .card--back { left: 617px; background: var(--card-light); }

  .front-brand {
    position: absolute;
    left: 0; right: 0;
    top: 100px;
    text-align: center;
  }
  .brand-square {
    display: inline-block;
    width: 22px; height: 22px;
    background: var(--brand-green);
    margin-bottom: 12px;
  }
  .brand-name {
    display: block;
    color: var(--brand-green);
    font-size: 31px;
    line-height: 1;
    letter-spacing: -0.3px;
  }
  .brand-tagline {
    display: block;
    color: var(--text-grey);
    font-size: 11px;
    margin-top: 4px;
  }

  .back-details {
    position: absolute;
    right: 38px;
    top: 118px;
    text-align: right;
  }
  .back-details .brand-square { width: 18px; height: 18px; margin-bottom: 14px; }
  .back-details .brand-name { font-size: 24px; }
  .back-details .brand-tagline { color: var(--text-dark-grey); font-size: 12px; margin-top: 2px; }
  .contact-list {
    list-style: none;
    margin-top: 22px;
    color: var(--text-dark-grey);
    font-size: 12px;
    line-height: 15px;
  }
  .contact-label { color: var(--brand-green); }
</style>
</head>
<body>
<main class="stage">
  <section class="card card--front">
    <div class="front-brand">
      <span class="brand-square" aria-hidden="true"></span>
      <span class="brand-name">Maren Dulworth</span>
      <span class="brand-tagline">Investor - Solutions - Development</span>
    </div>
  </section>

  <section class="card card--back">
    <div class="back-details">
      <span class="brand-square" aria-hidden="true"></span>
      <span class="brand-name">Maren Dulworth</span>
      <span class="brand-tagline">Creative property solutions</span>
      <ul class="contact-list">
        <li><span class="contact-label">T:</span> 0481 253 407 <span class="contact-label">F:</span> (07) 3584 2719</li>
        <li><span class="contact-label">E:</span> maren47@plx.com.au</li>
      </ul>
    </div>
  </section>
</main>
</body>
</html>
```